Brightvale Job Specifications

Pls create α professional Job Spec for the Services Agents Role for Brightvale so it looks professional for New Hires.

Target Market(s)

Company Employees

Requirements
Must have
• Professional look

```html
<!DOCTYPE html>
<html lang="en">
<head>
<meta charset="utf-8">
<title>Brightvale – Service Agent Job Specification</title>
<link href="https://fonts.googleapis.com/css2?family=Arimo:wght@400;700&display=swap" rel="stylesheet">
<style>
  :root {
    --navy: #1c3c6d;
    --ink: #1d1d1f;
    --rule: #8c8c8c;
    --frame: #1a1a1a;
    --paper: #ffffff;
  }
  * { box-sizing: border-box; margin: 0; padding: 0; }
  html, body {
    width: 1200px; height: 848px; overflow: hidden;
    background: var(--paper);
  }
  body {
    position: relative;
    font-family: "Arimo", "Helvetica Neue", Arial, sans-serif;
    color: var(--ink);
  }
  .brand {
    position: absolute; top: 50px; left: 0; width: 1200px;
    display: flex; justify-content: center; align-items: center; gap: 10px;
  }
  .brand-dot {
    width: 30px; height: 30px; border-radius: 50%;
    background: var(--navy);
  }
  .brand-name {
    font-size: 32px; font-weight: 700; color: var(--navy);
  }
  .spec {
    position: absolute; left: 112px; top: 147px; width: 954px;
    border-collapse: collapse; table-layout: fixed;
    border: 2px solid var(--frame);
    font-size: 13.3px; line-height: 16.8px;
  }
  .spec col.label { width: 196px; }
  .spec col.value { width: 253px; }
  .spec col.purpose { width: 505px; }
  .spec th {
    background: var(--navy); color: #fff;
    font-size: 16.5px; font-weight: 700; text-align: left;
    height: 30px; padding: 3px 6px 0;
    border-left: 1.5px solid #fff;
  }
  .spec th:first-child { border-left: none; }
  .spec td {
    vertical-align: top; padding: 4px 6px;
    border: 1px solid var(--rule);
  }
  .spec td.field { font-weight: 700; }
  .row-report td { height: 25px; }
  .row-location td { height: 430px; }
  .row-level td, .row-direct td { height: 25px; }
  .row-relations td { height: 72px; }
  .purpose-cell { padding-top: 5px !important; }
  .bullets { list-style: none; }
  .bullets > li { position: relative; padding-left: 19px; }
  .bullets > li::before {
    content: "•"; position: absolute; left: 1px; top: 0; font-size: 10px;
  }
  .portfolio { list-style: none; }
  .portfolio li { padding-left: 0; }
  .success-title {
    font-size: 16.5px; font-weight: 700; margin: 9px 0 1px;
  }
</style>
</head>
<body>
  <header class="brand">
    <span class="brand-dot"></span>
    <span class="brand-name">Brightvale</span>
  </header>

  <table class="spec">
    <colgroup>
      <col class="label"><col class="value"><col class="purpose">
    </colgroup>
    <thead>
      <tr>
        <th>JOB TITLE</th>
        <th>SERVICE AGENT</th>
        <th>PURPOSE: (HOW THE ROLE ADDS VALUE)</th>
      </tr>
    </thead>
    <tbody>
      <tr class="row-report">
        <td class="field">2. Reporting to</td>
        <td>Service and Operations Manager</td>
        <td class="purpose-cell" rowspan="2">
          <ul class="bullets">
            <li>Quality and Focused Cleaning and Maintenance Services across dedicated portfolios:
              <ul class="portfolio">
                <li>A)&nbsp; Brush Cleaning Services</li>
                <li>B)&nbsp; Gurney and Playground Services</li>
                <li>C)&nbsp; Detailed Kitchen Cleaning and Vat Boil Out Services.</li>
                <li>D)&nbsp; General Facility Maintenance.</li>
              </ul>
            </li>
            <li>Full brush cleaning service required for key customers.</li>
            <li>Quarterly Tune Up Kit Install</li>
            <li>All Online tracking in accordance to the TaskLoop app – Tracked on Smartphone.</li>
            <li>Filter of side of machines cleaned thoroughly.</li>
            <li>Outside of machine must be cleaned on each service in full.</li>
            <li>All Portfolio Services require thorough cleaning in accordance to the specific checklists and Standard Operating Manuals.</li>
            <li>Responsible for monitoring service standards and metrics.</li>
            <li>Responsible for reliability and on time scheduled services.</li>
            <li>Positive Approach to Team Members and Customer</li>
            <li>Customer Service Focused.</li>
            <li>Ensuring compliance with OHS and Hygiene Levels.</li>
            <li>Training new staff when necessary</li>
          </ul>
          <h2 class="success-title">What Success will look like in 2 years:</h2>
          <ul class="bullets">
            <li>New and retained clients, increase in market share and value</li>
            <li>Consistent roster and work for all resources</li>
            <li>Reporting and metrics delivery of quality and consistent work standards</li>
            <li>Operational growth for all workers involved.</li>
            <li>Increase in the number of resources supervising and mentoring.</li>
          </ul>
        </td>
      </tr>
      <tr class="row-location">
        <td class="field">3. Location:</td>
        <td>Local and surrounding area.</td>
      </tr>
      <tr class="row-level">
        <td class="field">4</td>
        <td>Cleaning Services Agent, Level 1.</td>
        <td></td>
      </tr>
      <tr class="row-direct">
        <td class="field">Direct Reports:</td>
        <td>N/A</td>
        <td></td>
      </tr>
      <tr class="row-relations">
        <td class="field">Key Relationships:</td>
        <td>
          <ul class="bullets">
            <li>Key clients.</li>
            <li>Head office management</li>
            <li>Operations management</li>
            <li>Client Relations Manager</li>
          </ul>
        </td>
        <td></td>
      </tr>
    </tbody>
  </table>
</body>
</html>
```